Wordpress Template for Food Retail Shop

We need a wordpress template that fits our new wp installation with about 6-7 sites. frontpage, news, team, products, contact. we provide food from local suppliers, * green * products. we provide a local bakery

```html
<!DOCTYPE html>
<html lang="en">
<head>
<meta charset="utf-8">
<title>Fernhill – Organic Food Store</title>
<link rel="stylesheet" href="https://fonts.googleapis.com/css2?family=Ubuntu:wght@400;500;700&family=Montserrat:wght@800;900&family=Open+Sans:ital,wght@0,400;0,600;0,700;1,400&family=Pacifico&family=Libre+Baskerville:ital@1&display=swap">
<style>
:root{
  --green:#8cc63f;
  --green-dark:#6fa82a;
  --orange:#f7a93b;
  --ink:#222;
  --text:#555;
  --muted:#888;
  --pale-blue:#f1f6fc;
  --cream:#f8f6e9;
  --footer:#1f1f1f;
  --footer-bar:#161616;
  --line:#e4e4e4;
}
*{box-sizing:border-box;margin:0;padding:0}
html,body{width:1200px;height:3561px;overflow:hidden}
body{position:relative;background:#fff;font-family:"Open Sans",sans-serif;color:var(--text)}
.abs{position:absolute}
.ph{position:absolute;border-radius:6px}
a{color:inherit;text-decoration:none}

/* header */
.site-header{position:absolute;left:0;top:0;width:1200px;height:470px;background:linear-gradient(#eef4fb 0,#eef4fb 95px,#eceeef 95px,#f3f3f3 100%)}
.brand{position:absolute;display:flex;align-items:center;gap:8px;font-family:"Ubuntu",sans-serif;font-weight:500;color:var(--green)}
.brand .dot{width:32px;height:32px;border-radius:50%;background:var(--orange)}
.header-brand{left:235px;top:29px;font-size:31px}
.contact-item{position:absolute;top:24px;display:flex;gap:10px;font-size:10px;line-height:15px;color:var(--text)}
.contact-item b{display:block;color:var(--ink);font-weight:600}
.ci-icon{width:26px;height:26px;border-radius:50%;background:#fff;display:flex;align-items:center;justify-content:center;flex:none}
.main-nav{position:absolute;left:487px;top:79px;width:478px;height:36px;background:#fff;border-radius:18px;box-shadow:0 2px 8px rgba(0,0,0,.06);display:flex;align-items:center;padding:0 28px;gap:0;font-size:9px;color:var(--ink);font-weight:600;justify-content:space-between}
.main-nav .active{color:var(--green);border-bottom:2px solid var(--green);padding-bottom:3px}

.hero-art-left{left:0;top:95px;width:460px;height:375px;background:radial-gradient(ellipse at 40% 40%,#f2f2f4,#a9cf7a 80%);opacity:.55;border-radius:0}
.hero-art-right{left:700px;top:95px;width:500px;height:375px;background:radial-gradient(ellipse at 60% 65%,#f3b04b 0,#8cc44e 45%,#eef0ef 78%);opacity:.75;border-radius:0}
.hero-script{left:0;width:1200px;top:200px;text-align:center;font-family:"Pacifico",cursive;font-size:32px;color:var(--orange);padding-left:10px}
.hero-title{left:0;width:1200px;top:246px;text-align:center;font-family:"Montserrat",sans-serif;font-weight:900;font-size:32px;color:#111}
.hero-sub{left:0;width:1200px;top:288px;text-align:center;font-size:13px;color:var(--ink)}
.pill-btn{position:absolute;height:37px;border-radius:19px;background:linear-gradient(90deg,var(--green),var(--green-dark));color:#fff;font-size:11px;font-weight:700;display:flex;align-items:center;padding-left:52px}
.pill-btn .knob{position:absolute;left:-2px;top:-2px;width:41px;height:41px;border-radius:50%;background:#fff;box-shadow:0 0 0 4px var(--orange) inset}
.torn{position:absolute;left:0;top:455px;width:1200px;height:18px}

/* about */
.about-back{left:260px;top:570px;width:310px;height:355px;background:var(--green)}
.about-photo{left:235px;top:545px;width:311px;height:355px;background:linear-gradient(150deg,#4c6b2c,#8fa651 45%,#c9583a 75%,#d8c38c);border-radius:4px}
.play{left:361px;top:695px;width:56px;height:56px;border-radius:50%;background:#fff}
.about-heading{left:610px;top:588px;font-family:"Ubuntu",sans-serif;font-weight:500;font-size:22px;line-height:31px;color:var(--ink)}
.about-lead{left:610px;top:655px;width:360px;font-family:"Ubuntu",sans-serif;font-size:12.5px;line-height:18px;color:var(--green)}
.about-text{left:610px;top:700px;width:360px;font-size:8.6px;line-height:15px;color:var(--text)}
.delivery{left:610px;top:817px;width:294px;height:100px;background:var(--orange);border-radius:6px;color:#fff;padding:22px 26px}
.delivery small{display:block;font-family:"Ubuntu",sans-serif;font-size:14px;font-weight:500}
.delivery strong{display:block;font-family:"Ubuntu",sans-serif;font-size:27px;font-weight:700;margin-top:4px}
.delivery-icon{left:869px;top:839px;width:56px;height:56px;border-radius:50%;background:var(--orange);border:3px solid #fff;display:flex;align-items:center;justify-content:center}

/* shared section title */
.section-title{position:absolute;left:0;width:1200px;text-align:center;font-family:"Ubuntu",sans-serif;font-weight:500;font-size:22px;color:var(--ink)}
.section-title::after{content:"";display:block;width:38px;height:2px;background:var(--green);margin:14px auto 0}

/* products */
.products{left:0;top:998px;width:1200px;height:794px;background:var(--pale-blue)}
.product-card{position:absolute;width:169px;height:249px;background:#fff}
.product-card .thumb{position:absolute;left:25px;top:30px;width:119px;height:130px;border-radius:50%}
.product-card .name{position:absolute;left:0;right:0;top:189px;text-align:center;font-family:"Ubuntu",sans-serif;font-weight:500;font-size:15px;color:var(--ink)}
.t-cauli{background:radial-gradient(circle,#eef0df 0 35%,#6fae3f 60%,transparent 72%)}
.t-cheese{background:radial-gradient(circle,#f6d66a 0 55%,transparent 70%)}
.t-blue{background:radial-gradient(ellipse at 50% 60%,#dfe4e8 0 35%,#6b4a32 50%,transparent 62%)}
.t-carrot{background:radial-gradient(circle at 55% 30%,#3d8a2c 0 25%,transparent 35%),radial-gradient(ellipse at 40% 70%,#f08a23 0 30%,transparent 45%)}
.deco{position:absolute;border-radius:50%}

/* team */
.member{position:absolute;width:169px;top:1935px;height:257px;border-bottom:1px solid var(--line);text-align:center}
.member .photo{width:150px;height:190px;margin:0 auto;border-radius:6px;background:linear-gradient(180deg,#f1ead9 0,#c98d5a 35%,#3e6fb8 70%,#fff 100%)}
.member .name{margin-top:24px;font-size:9.5px;color:var(--ink)}
.member .role{margin-top:7px;font-size:8px;color:var(--muted)}

/* testimonials */
.testimonials{left:0;top:2252px;width:1200px;height:333px;background:var(--cream)}
.avatar{left:570px;top:2364px;width:60px;height:60px;border-radius:50%;background:linear-gradient(#8a6a4e,#e4c3a5)}
.arrow{position:absolute;top:2386px;width:14px;height:16px}
.quote{left:290px;top:2448px;width:620px;text-align:center;font-family:"Libre Baskerville",serif;font-style:italic;font-size:10.2px;line-height:18px;color:#444}
.q-name{left:0;width:1200px;top:2514px;text-align:center;font-size:9px;font-weight:700;color:var(--ink)}
.q-role{left:0;width:1200px;top:2529px;text-align:center;font-size:8.5px;color:var(--muted)}

/* partners */
.partners{left:236px;top:2645px;width:729px;height:86px;border:1px solid var(--line);display:flex}
.partners .cell{flex:1;border-right:1px solid var(--line);display:flex;align-items:center;justify-content:center}
.partners .cell:last-child{border-right:0}
.badge{width:70px;height:40px;background:#d9d9d9;border-radius:4px}
.badge.round{width:56px;height:56px;border-radius:50%}
.dots{left:584px;top:2759px;display:flex;gap:4px}
.dots i{display:block;width:6px;height:6px;border-radius:3px;background:#ccc}
.dots i.on{width:16px;background:var(--green)}

/* news */
.news-card{position:absolute;top:2907px;width:231px}
.news-card .img{height:130px;border-radius:4px;position:relative}
.news-card .date{position:absolute;left:20px;top:62px;width:54px;height:54px;border-radius:50%;background:var(--green);color:#fff;font-size:10px;text-align:center;line-height:13px;padding-top:14px}
.news-card .meta{margin-top:21px;font-size:7.5px;color:var(--ink);padding-left:4px}
.news-card .meta span{color:var(--green)}
.news-card h3{margin-top:12px;font-size:10px;line-height:17px;font-weight:600;color:var(--ink)}
.news-card p{margin-top:4px;font-size:8.5px;line-height:15px;color:var(--text)}
.news-card .more{display:inline-block;margin-top:6px;font-size:8.5px;color:var(--green);text-decoration:underline}

/* footer */
.site-footer{left:0;top:3228px;width:1200px;height:279px;background:var(--footer);color:#ddd}
.footer-brand{left:235px;top:3285px;font-size:28px}
.footer-about{left:235px;top:3328px;width:230px;font-size:8.3px;line-height:16.2px;color:#ddd}
.f-col{position:absolute;top:3287px}
.f-col h4{font-size:9.5px;font-weight:700;color:#fff;letter-spacing:.2px}
.f-col h4::after{content:"";display:block;width:22px;height:2px;background:var(--orange);margin-top:8px}
.f-col ul{list-style:none;margin-top:17px}
.f-col li{font-size:8.5px;line-height:22.5px;color:#ddd}
.f-col li::before{content:"";display:inline-block;width:10px;height:1px;background:#999;vertical-align:middle;margin-right:9px}
.f-contact{position:absolute;left:799px;top:3329px;font-size:8.5px;line-height:14px;color:#ddd}
.f-contact div{display:flex;gap:10px;align-items:flex-start;margin-bottom:14px}
.f-contact svg{flex:none}
.footer-bar{left:0;top:3507px;width:1200px;height:54px;background:var(--footer-bar)}
.copyright{left:235px;top:3529px;font-size:8px;color:#bbb}
.social{position:absolute;top:3522px;width:26px;height:26px;border-radius:50%;border:1.5px solid #ddd}
</style>
</head>
<body>

<header class="site-header">
  <div class="ph hero-art-left" role="img" aria-label="Mesh produce bags filled with vegetables, spinach leaves and a tomato"></div>
  <div class="ph hero-art-right" role="img" aria-label="Mango, avocado, grapes, cherries and leafy greens"></div>

  <div class="brand header-brand"><span class="dot"></span>Fernhill</div>

  <div class="contact-item" style="left:503px">
    <span class="ci-icon"><svg width="12" height="12" viewBox="0 0 24 24"><path d="M6.6 10.8a15 15 0 0 0 6.6 6.6l2.2-2.2a1 1 0 0 1 1-.3 11 11 0 0 0 3.6.6 1 1 0 0 1 1 1V20a1 1 0 0 1-1 1A17 17 0 0 1 3 4a1 1 0 0 1 1-1h3.5a1 1 0 0 1 1 1c0 1.2.2 2.4.6 3.6a1 1 0 0 1-.3 1z" fill="#8cc63f"/></svg></span>
    <div><b>Call Us</b>(555) 014 2290</div>
  </div>
  <div class="contact-item" style="left:633px">
    <span class="ci-icon"><svg width="12" height="12" viewBox="0 0 24 24"><path d="M3 5h18v14H3z" fill="#8cc63f"/><path d="M3 5l9 7 9-7" stroke="#fff" stroke-width="2" fill="none"/></svg></span>
    <div><b>Email Us</b>info@fernhill.com</div>
  </div>
  <div class="contact-item" style="left:770px">
    <span class="ci-icon"><svg width="12" height="12" viewBox="0 0 24 24"><path d="M12 2a7 7 0 0 0-7 7c0 5 7 13 7 13s7-8 7-13a7 7 0 0 0-7-7zm0 9.5A2.5 2.5 0 1 1 12 6.5a2.5 2.5 0 0 1 0 5z" fill="#8cc63f"/></svg></span>
    <div><b>Address</b>48 Orchard Lane, Greenfield Valley<br>Northshire, United Kingdom</div>
  </div>

  <nav class="main-nav">
    <a class="active">HOME</a><a>ABOUT US</a><a>PRODUCTS</a><a>NEWS</a><a>TEAM</a><a>CONTACT US</a>
    <svg width="11" height="11" viewBox="0 0 24 24"><circle cx="10" cy="10" r="6.5" stroke="#8cc63f" stroke-width="2.5" fill="none"/><path d="M15 15l6 6" stroke="#8cc63f" stroke-width="2.5"/></svg>
  </nav>

  <div class="abs hero-script">Fresh Look</div>
  <h1 class="abs hero-title">100% ORGANIC</h1>
  <p class="abs hero-sub">Farm Green Products Right to Your Door</p>
  <a class="pill-btn" style="left:520px;top:325px;width:142px"><span class="knob"></span>CONTACT US</a>

  <svg class="torn" viewBox="0 0 1200 18" preserveAspectRatio="none"><path d="M0 10 L40 6 L80 12 L130 5 L180 11 L240 4 L300 12 L360 6 L420 11 L480 5 L540 12 L600 7 L660 11 L720 4 L780 12 L840 6 L900 11 L960 5 L1020 12 L1080 6 L1140 11 L1200 5 V18 H0Z" fill="#fff"/></svg>
</header>

<section>
  <div class="abs about-back"></div>
  <div class="ph about-photo" role="img" aria-label="Basket of freshly harvested vegetables: cabbage, tomato, onions and leeks"></div>
  <svg class="abs" style="left:361px;top:695px" width="56" height="56" viewBox="0 0 56 56"><circle cx="28" cy="28" r="28" fill="#fff"/><path d="M22 18 L38 28 L22 38Z" fill="#f7a93b"/></svg>
  <h2 class="abs about-heading">We Provide<br>High-Quality Organic Products</h2>
  <p class="abs about-lead">Lorem ipsum dolor sit amet, consectetur adipiscing elit. Phasellus at pharetra metus</p>
  <p class="abs about-text">Vestibulum vel dui sodales, convallis eros vitae, rutrum mauris. Proin eget justo at massa egestas varius. Praesent tincidunt nisi et turpis suscipit, eget feugiat ligula dignissim. Curabitur porttitor euismod lacinia. Sed lorem tellus, commodo at pretium ut, ultricies nec elit. Vivamus sit amet turpis ut nibh dictum suscipit. Vivamus pellentesque neque metus, quis feugiat sem maximus in. Fusce pellentesque mollis placerat. Nulla at convallis arcu, sit amet vehicula magna.</p>
  <div class="abs delivery"><small>Call Us on Delivery</small><strong>(555) 014 2290</strong></div>
  <div class="abs delivery-icon"><svg width="20" height="20" viewBox="0 0 24 24"><path d="M6.6 10.8a15 15 0 0 0 6.6 6.6l2.2-2.2a1 1 0 0 1 1-.3 11 11 0 0 0 3.6.6 1 1 0 0 1 1 1V20a1 1 0 0 1-1 1A17 17 0 0 1 3 4a1 1 0 0 1 1-1h3.5a1 1 0 0 1 1 1c0 1.2.2 2.4.6 3.6a1 1 0 0 1-.3 1z" fill="none" stroke="#fff" stroke-width="1.5"/></svg></div>
</section>

<section class="abs products">
  <div class="deco" role="img" aria-label="Orange slice" style="left:48px;top:648px;width:34px;height:34px;background:#f6a13a"></div>
  <div class="deco" role="img" aria-label="Herb sprig" style="left:80px;top:690px;width:120px;height:100px;background:radial-gradient(#a9d07a,transparent 70%)"></div>
  <div class="deco" role="img" aria-label="Herb sprig" style="left:1070px;top:620px;width:120px;height:100px;background:radial-gradient(#a9d07a,transparent 70%)"></div>
  <div class="deco" role="img" aria-label="Cherries" style="left:974px;top:748px;width:26px;height:26px;background:#d0262f"></div>
  <div class="deco" role="img" aria-label="Orange slice" style="left:1090px;top:760px;width:50px;height:50px;background:#f6a13a"></div>
</section>
<h2 class="section-title" style="top:1048px">Our Products</h2>

<div class="product-card" style="left:235px;top:1130px"><div class="thumb t-cauli" role="img" aria-label="Cauliflower"></div><div class="name">Cauliflower</div></div>
<div class="product-card" style="left:423px;top:1130px"><div class="thumb t-cheese" role="img" aria-label="Wedge of holland cheese"></div><div class="name">Cheese Holand</div></div>
<div class="product-card" style="left:611px;top:1130px"><div class="thumb t-blue" role="img" aria-label="Blue cheese on a board"></div><div class="name">Cheese</div></div>
<div class="product-card" style="left:798px;top:1130px"><div class="thumb t-carrot" role="img" aria-label="Bunch of carrots"></div><div class="name">Carrots</div></div>
<div class="product-card" style="left:235px;top:1399px"><div class="thumb t-cauli" role="img" aria-label="Cauliflower"></div><div class="name">Cauliflower</div></div>
<div class="product-card" style="left:423px;top:1399px"><div class="thumb t-cheese" role="img" aria-label="Wedge of holland cheese"></div><div class="name">Cheese Holand</div></div>
<div class="product-card" style="left:611px;top:1399px"><div class="thumb t-blue" role="img" aria-label="Blue cheese on a board"></div><div class="name">Cheese</div></div>
<div class="product-card" style="left:798px;top:1399px"><div class="thumb t-carrot" role="img" aria-label="Bunch of carrots"></div><div class="name">Carrots</div></div>

<a class="pill-btn" style="left:532px;top:1691px;width:140px"><span class="knob"></span>VIEW MORE</a>

<h2 class="section-title" style="top:1845px">Expert Team</h2>
<div class="member" style="left:235px"><div class="photo" role="img" aria-label="Farmer in straw hat holding a basket of oranges"></div><div class="name">OWEN HARTLEY</div><div class="role">Our Team</div></div>
<div class="member" style="left:423px"><div class="photo" role="img" aria-label="Farmer holding a basket of vegetables"></div><div class="name">CLARA BELLAMY</div><div class="role">Our Team</div></div>
<div class="member" style="left:611px"><div class="photo" role="img" aria-label="Young farmer holding a crate of produce"></div><div class="name">LEO MARSH</div><div class="role">Our Team</div></div>
<div class="member" style="left:798px"><div class="photo" role="img" aria-label="Farmer holding a basket of vegetables"></div><div class="name">SAM WHITAKER</div><div class="role">Our Team</div></div>

<section class="abs testimonials">
  <div class="deco" role="img" aria-label="Scattered peppercorns" style="left:70px;top:30px;width:135px;height:110px;background:radial-gradient(#b06a3e,transparent 70%)"></div>
  <div class="deco" role="img" aria-label="Potatoes, garlic and sausages" style="left:0;top:200px;width:400px;height:150px;background:radial-gradient(ellipse at 35% 70%,#c8924f,transparent 65%)"></div>
  <div class="deco" role="img" aria-label="Falling salad leaves and a fork" style="left:870px;top:0;width:240px;height:330px;background:radial-gradient(ellipse,#7fbf4a,transparent 65%)"></div>
</section>
<h2 class="section-title" style="top:2298px">What Customers Say</h2>
<div class="abs avatar" role="img" aria-label="Customer portrait"></div>
<svg class="arrow" style="left:546px" viewBox="0 0 14 16"><path d="M9 3 L4 8 L9 13" stroke="#f7a93b" stroke-width="1.5" fill="none"/></svg>
<svg class="arrow" style="left:643px" viewBox="0 0 14 16"><path d="M5 3 L10 8 L5 13" stroke="#f7a93b" stroke-width="1.5" fill="none"/></svg>
<p class="abs quote">Lorem ipsum dolor sit amet, consectetur adipiscing elit. Cras vitae sagittis lectus. Aliquam erat volutpat. Etiam eu suscipit lorem. Ut eget massa venenatis, pellentesque nibh et, fermentum odio. Sed in cursus urna. Quisque eu mi tortor. Pellentesque cursus turpis tellus, semper vehicula justo ornare vel. Fusce imperdiet interdum felis.</p>
<div class="abs q-name">NORA FIELDING</div>
<div class="abs q-role">Cras orci nisl</div>

<div class="abs partners">
  <div class="cell"><span class="badge round"></span></div>
  <div class="cell"><span class="badge"></span></div>
  <div class="cell"><span class="badge"></span></div>
  <div class="cell"><span class="badge"></span></div>
  <div class="cell"><span class="badge"></span></div>
</div>
<div class="abs dots"><i class="on"></i><i></i><i></i></div>

<h2 class="section-title" style="top:2819px">Latest News</h2>
<article class="news-card" style="left:235px">
  <div class="img" role="img" aria-label="Woman picking berries in a garden" style="background:linear-gradient(135deg,#2f3d22,#6a7a3c 50%,#c25d6a)"><span class="date">22<br>Oct</span></div>
  <div class="meta">Posted by <span>admin</span> &nbsp;&nbsp; <span>4 Comments</span></div>
  <h3>LOREM IPSUM DOLOR SIT AMET, CONSECTETUR ADIPISCING ELIT.</h3>
  <p>Duis rhoncus mauris ipsum, et vulputate erat imperdiet accumsan. Suspendisse potenti.</p>
  <a class="more">Read More</a>
</article>
<article class="news-card" style="left:485px">
  <div class="img" role="img" aria-label="Hands holding fresh blueberries" style="background:linear-gradient(135deg,#5c7fa6,#232a45 55%,#8f6b5b)"><span class="date">22<br>Oct</span></div>
  <div class="meta">Posted by <span>admin</span> &nbsp;&nbsp; <span>4 Comments</span></div>
  <h3>LOREM IPSUM DOLOR SIT AMET, CONSECTETUR ADIPISCING ELIT.</h3>
  <p>Duis rhoncus mauris ipsum, et vulputate erat imperdiet accumsan. Suspendisse potenti.</p>
  <a class="more">Read More</a>
</article>
<article class="news-card" style="left:735px">
  <div class="img" role="img" aria-label="Green smoothie with banana, avocado and citrus" style="background:linear-gradient(135deg,#3b3f3a,#6d8a3a 45%,#e5b84a 75%,#5c4a36)"><span class="date">22<br>Oct</span></div>
  <div class="meta">Posted by <span>admin</span> &nbsp;&nbsp; <span>4 Comments</span></div>
  <h3>LOREM IPSUM DOLOR SIT AMET, CONSECTETUR ADIPISCING ELIT.</h3>
  <p>Duis rhoncus mauris ipsum, et vulputate erat imperdiet accumsan. Suspendisse potenti.</p>
  <a class="more">Read More</a>
</article>

<footer>
  <div class="abs site-footer"></div>
  <div class="brand footer-brand"><span class="dot"></span>Fernhill</div>
  <p class="abs footer-about">Lorem ipsum dolor sit amet, consectetur adipiscing elit. In nulla urna, faucibus id pellentesque quis, ultricies hendrerit est. Fusce arcu erat, pellentesque in dolor sed, pulvinar suscipit libero. Vestibulum vehicula purus eu scelerisque vulputate. Pellentesque diam lorem, tristique in arcu quis, luctus tincidunt risus. Phasellus dapibus elit vitae sodales pretium.</p>
  <div class="f-col" style="left:507px"><h4>QUICK LINKS</h4><ul><li>Home</li><li>About us</li><li>Products</li><li>Team</li><li>News</li><li>Contact us</li></ul></div>
  <div class="f-col" style="left:633px"><h4>OTHER LINKS</h4><ul><li>Testimonials</li><li>Terms &amp; Conditions</li><li>Privacy Policy</li><li>Site Map</li><li>FAQs</li></ul></div>
  <div class="f-col" style="left:799px"><h4>CONTACT INFO</h4></div>
  <div class="f-contact">
    <div><svg width="14" height="16" viewBox="0 0 24 24"><path d="M12 2a7 7 0 0 0-7 7c0 5 7 13 7 13s7-8 7-13a7 7 0 0 0-7-7z" fill="none" stroke="#8cc63f" stroke-width="1.6"/><circle cx="12" cy="9" r="2.5" fill="#8cc63f"/></svg><span>48 Orchard Lane, Greenfield Valley<br>Northshire, United Kingdom</span></div>
    <div><svg width="14" height="18" viewBox="0 0 14 18"><rect x="2" y="1" width="10" height="16" rx="1.5" fill="none" stroke="#8cc63f" stroke-width="1.4"/><circle cx="7" cy="14" r="1" fill="#8cc63f"/></svg><span>(555) 014 2290</span></div>
    <div><svg width="16" height="14" viewBox="0 0 16 14"><rect x="1" y="2" width="14" height="10" fill="none" stroke="#8cc63f" stroke-width="1.4"/><path d="M1 2l7 6 7-6" fill="none" stroke="#8cc63f" stroke-width="1.4"/></svg><span>info@fernhill.com</span></div>
  </div>
  <div class="abs footer-bar"></div>
  <p class="abs copyright">Copyright © 2019 Fernhill. All Rights Reserved. Privacy Policy | Terms of Service</p>
  <span class="social" style="left:845px"></span>
  <span class="social" style="left:877px"></span>
  <span class="social" style="left:909px"></span>
  <span class="social" style="left:941px"></span>
</footer>

</body>
</html>
```